Best local air conditioning and heating contractor

We need a website design for a new company in Tampa Bay called The Brightwell Cooling Company. We provide superior services for residential and commercial properties as well as maintenance and installing HVAC systems. We also want to sell equipment, parts and filter on the website as well. We want it easy to use for customers. Rich with content and keywords for our area.

Target Market(s)

homeowners in Tampa Bay

Industry/Entity Type

HVAC air conditioning and heating

Coding

Coded - Design and coding required

Number of Pages Required

5+ page

Font styles to use
Sans Serif

Requirements
Nice to have
• would like the colors to be same as logo

```html
<!DOCTYPE html>
<html lang="en">
<head>
<meta charset="utf-8">
<title>About Us – Brightwell Cooling Company</title>
<link rel="stylesheet" href="https://fonts.googleapis.com/css2?family=Outfit:wght@300;400;500;600;700&family=Syncopate:wght@700&display=swap">
<style>
:root{
  --navy:#22306b;
  --navy-deep:#1d2a63;
  --red:#d71f26;
  --ink:#111111;
  --text:#333333;
  --white:#ffffff;
  --gold:#f5c518;
}
*{margin:0;padding:0;box-sizing:border-box}
html,body{width:1200px;height:2511px;overflow:hidden}
body{position:relative;font-family:"Outfit",sans-serif;color:var(--text);background:var(--white)}
.abs{position:absolute}
.display{font-family:"Syncopate",sans-serif;font-weight:700;letter-spacing:1px;text-transform:uppercase}

/* top bar */
.topbar{left:0;top:0;width:1200px;height:28px;background:var(--navy);color:var(--white);font-size:12px;font-weight:500}
.topbar .item{position:absolute;top:7px;display:flex;align-items:center;gap:5px}
.topbar .sep{position:absolute;top:6px;width:1px;height:16px;background:rgba(255,255,255,.35)}
.social-dot{position:absolute;top:7px;width:13px;height:13px;border-radius:50%;background:var(--white)}

/* header */
.header{left:0;top:28px;width:1200px;height:77px;background:var(--white)}
.brand{position:absolute;left:101px;top:26px;display:flex;align-items:center;gap:8px;font-size:17px;font-weight:700;color:var(--navy)}
.brand .mark{width:20px;height:20px;border-radius:50%;background:var(--red)}
.nav{position:absolute;top:31px;display:flex;gap:0;font-size:15px;font-weight:600;color:var(--ink)}
.nav span{position:absolute;white-space:nowrap}
.callbox{position:absolute;left:885px;top:0;width:315px;height:77px;background:var(--red);clip-path:polygon(26px 0,100% 0,100% 100%,0 100%)}
.callbox .icon{position:absolute;left:-12px;top:12px;width:50px;height:50px;border-radius:50%;background:var(--white)}
.callbox .lbl{position:absolute;left:51px;top:11px;color:var(--white);font-size:17px}
.callbox .num{position:absolute;left:51px;top:33px;color:var(--white);font-size:32px;font-weight:700;letter-spacing:.5px}

/* hero */
.hero{left:0;top:105px;width:1200px;height:312px;background:linear-gradient(90deg,rgba(180,30,40,.85),rgba(90,80,90,.75) 55%,rgba(150,40,50,.85)),linear-gradient(#4a4f55,#2b2e33)}
.hero h1{position:absolute;left:0;width:1200px;top:163px;text-align:center;color:var(--white);font-size:34px}

/* photos */
.photo{position:absolute;background:linear-gradient(135deg,#8a8f96,#3a3f48)}
.frame{position:absolute;background:var(--red)}

/* section headings */
.heading{font-size:31px;color:var(--ink);line-height:1}
.heading em{font-style:normal;color:var(--red)}
.underline{position:absolute;height:4px;width:90px;background:var(--red)}
.copy{font-size:15px;line-height:25.6px;text-align:justify;color:var(--text)}
.list{list-style:none;font-size:15px;line-height:25.6px}
.list li{display:flex;align-items:center;gap:7px}
.list svg{flex:none}

/* banner */
.banner{left:0;top:1582px;width:1200px;height:558px;background:linear-gradient(90deg,#8b95a8,#d9dde3 25%,#eef0f3 60%,#b9c0ca)}
.card{position:absolute;left:187px;top:1675px;width:826px;height:375px;background:rgba(255,255,255,.92);border-top:3px solid var(--red);text-align:center}
.card h2{margin-top:50px;font-size:33px;line-height:34px;color:var(--ink)}
.card h2 em{font-style:normal;color:var(--red)}
.card .sub{margin-top:40px;font-size:17px;font-weight:500;color:var(--ink)}
.card .copy{margin:10px auto 0;width:716px;text-align:justify;text-align-last:center}

/* footer */
.rule{left:0;top:2140px;width:1200px;height:5px;background:var(--red)}
.footer{left:0;top:2145px;width:1200px;height:366px;background:var(--navy-deep);color:var(--white)}
.footer .fbrand{position:absolute;left:106px;top:105px;display:flex;align-items:center;gap:8px;font-size:22px;font-weight:700}
.footer .fbrand .mark{width:24px;height:24px;border-radius:50%;background:var(--white)}
.fsoc{position:absolute;top:208px;width:38px;height:38px;border-radius:50%;background:var(--white)}
.col{position:absolute;top:70px}
.col h3{font-size:18px;font-weight:600;margin-bottom:12px}
.col p{font-size:13.5px;line-height:31px}
.footer .line{position:absolute;left:100px;top:294px;width:1000px;height:1px;background:rgba(255,255,255,.45)}
.footer .copyr{position:absolute;left:0;width:1200px;top:322px;text-align:center;font-size:15px}
</style>
</head>
<body>

<div class="abs topbar">
  <div class="item" style="left:101px"><span style="color:var(--gold);letter-spacing:-1px">★★★★★</span> 4.8 STAR SERVICES (20REVIEWS)</div>
  <div class="sep" style="left:365px"></div>
  <div class="item" style="left:375px">
    <svg width="11" height="11" viewBox="0 0 12 12"><circle cx="6" cy="6" r="5" fill="none" stroke="#e33" stroke-width="1.6"/><path d="M6 3v3l2 1" stroke="#e33" stroke-width="1.4" fill="none"/></svg>
    Mon to Fri 9:00 am to 6:00 pm</div>
  <div class="item" style="left:802px">
    <svg width="8" height="11" viewBox="0 0 8 11"><path d="M4 0a4 4 0 0 1 4 4c0 3-4 7-4 7S0 7 0 4a4 4 0 0 1 4-4z" fill="#e33"/></svg>
    Serving The Tampa Bay Area</div>
  <div class="sep" style="left:980px"></div>
  <div class="social-dot" style="left:990px"></div>
  <div class="sep" style="left:1012px"></div>
  <div class="social-dot" style="left:1020px"></div>
  <div class="sep" style="left:1042px"></div>
  <div class="social-dot" style="left:1053px"></div>
  <div class="sep" style="left:1075px"></div>
  <div class="social-dot" style="left:1086px"></div>
</div>

<header class="abs header">
  <div class="brand"><span class="mark"></span>Brightwell Cooling Company</div>
  <nav class="nav">
    <span style="left:375px">ABOUT US</span>
    <span style="left:477px">SERVICES</span>
    <span style="left:575px">HVAC</span>
    <span style="left:647px">RESOURCES</span>
    <span style="left:763px">CONTACT</span>
  </nav>
  <div class="callbox" style="overflow:visible;clip-path:none;background:none">
    <div style="position:absolute;inset:0;background:var(--red);clip-path:polygon(26px 0,100% 0,100% 100%,0 100%)"></div>
    <div class="icon" style="left:-10px;background:var(--navy);border:5px solid var(--white)">
      <svg width="40" height="40" viewBox="0 0 40 40"><path d="M14 12c1-1 2-1 3 0l2 3c.5 1 0 2-1 2.5-.5.5 0 2 1.5 3.5s3 2 3.5 1.5c.5-1 1.5-1.5 2.5-1l3 2c1 1 1 2 0 3l-1.5 1.5c-2 2-7 0-10.5-3.5S11 16 13 14z" fill="#fff"/></svg>
    </div>
    <div class="lbl">Call Today for Service</div>
    <div class="num">813 - 555 - 0192</div>
  </div>
</header>

<section class="abs hero" role="img" aria-label="Outdoor air conditioning condenser units beside a house wall, tinted red">
  <h1 class="display" style="position:absolute;top:163px">About Us</h1>
</section>

<!-- Our Story -->
<div class="frame" style="left:94px;top:493px;width:467px;height:459px"></div>
<div class="photo" role="img" aria-label="Two technicians servicing an outdoor AC condenser unit" style="left:106px;top:505px;width:466px;height:459px;background:linear-gradient(135deg,#b9a98a,#55565a 60%,#2c2f35)"></div>

<h2 class="abs display heading" style="left:650px;top:578px">Our <em>Story</em></h2>
<div class="underline" style="left:650px;top:616px"></div>
<p class="abs copy" style="left:650px;top:640px;width:455px">The Brightwell Cooling Company is a family-owned and operated company that provides professional heating, ventilation, and AC services in West Tampa. With over 70 years of combined experience and thousands of customers served, we have worked hard to earn a reputation of reliable workmanship, true quality, honesty, and dedication to customer service – all with a personal family touch. We provide 24/7 air conditioning services with no overtime charges and flat rate repairs for your peace of mind. Our trucks are fully stocked and ready to go the moment you need service and our professionals strive to arrive as quickly as possible.</p>

<!-- HVAC Repair -->
<h2 class="abs display heading" style="left:100px;top:1077px">HVAC <em>Repair</em></h2>
<div class="underline" style="left:100px;top:1114px"></div>
<p class="abs copy" style="left:100px;top:1133px;width:458px">The Brightwell Cooling Company is the Tampa Bay HVAC company you can count on for all heating and air conditioning issues. Our HVAC technicians are trained to handle a variety of heating and cooling systems. We can help keep you and your home as comfortable as possible with the following services:</p>
<ul class="abs list" style="left:100px;top:1261px">
  <li><svg width="13" height="13" viewBox="0 0 14 14"><circle cx="7" cy="7" r="5.5" fill="none" stroke="#d71f26" stroke-width="2"/><circle cx="7" cy="7" r="2" fill="#d71f26"/></svg>Heat Pump</li>
  <li><svg width="13" height="13" viewBox="0 0 14 14"><circle cx="7" cy="7" r="5.5" fill="none" stroke="#d71f26" stroke-width="2"/><circle cx="7" cy="7" r="2" fill="#d71f26"/></svg>Duct Work</li>
  <li><svg width="13" height="13" viewBox="0 0 14 14"><circle cx="7" cy="7" r="5.5" fill="none" stroke="#d71f26" stroke-width="2"/><circle cx="7" cy="7" r="2" fill="#d71f26"/></svg>Air Conditioning Repairs and Tune-Up</li>
  <li><svg width="13" height="13" viewBox="0 0 14 14"><circle cx="7" cy="7" r="5.5" fill="none" stroke="#d71f26" stroke-width="2"/><circle cx="7" cy="7" r="2" fill="#d71f26"/></svg>Air Conditioning Replacement and Installation</li>
  <li><svg width="13" height="13" viewBox="0 0 14 14"><circle cx="7" cy="7" r="5.5" fill="none" stroke="#d71f26" stroke-width="2"/><circle cx="7" cy="7" r="2" fill="#d71f26"/></svg>Refrigerant Check</li>
  <li><svg width="13" height="13" viewBox="0 0 14 14"><circle cx="7" cy="7" r="5.5" fill="none" stroke="#d71f26" stroke-width="2"/><circle cx="7" cy="7" r="2" fill="#d71f26"/></svg>Coil Cleaning</li>
  <li><svg width="13" height="13" viewBox="0 0 14 14"><circle cx="7" cy="7" r="5.5" fill="none" stroke="#d71f26" stroke-width="2"/><circle cx="7" cy="7" r="2" fill="#d71f26"/></svg>Condensing Unit</li>
</ul>
<div class="frame" style="left:632px;top:1028px;width:467px;height:460px"></div>
<div class="photo" role="img" aria-label="Technician replacing an air filter in an indoor air handler with insulated ducts" style="left:621px;top:1040px;width:466px;height:460px;background:linear-gradient(135deg,#e2e4e7,#9da2aa 50%,#3b3e45)"></div>

<!-- Banner -->
<section class="abs banner" role="img" aria-label="Blurred photo of a technician working on an AC unit"></section>
<div class="card">
  <h2 class="display">Brightwell Cooling<br><em>Conditioning Repair</em></h2>
  <div style="width:62px;height:3px;background:var(--red);margin:12px auto 0"></div>
  <p class="sub" style="margin-top:18px">Serving Odessa,&nbsp; Tampa, Westchase &amp; surrounding areas.</p>
  <p class="copy">Whether you need an emergency repair or a routine maintenance check on your heating or cooling unit, turn to Brightwell Cooling. We are a full-service, family-owned and operated company that provides reliable AC services in Palm Harbor and the surrounding areas. Our team of professionals is expertly trained to handle all your heating, ventilation, and air conditioning needs. We strive to exceed expectations by making sure our residential and commercial customers receive the very best in heating and air conditioning services. home ac repair air conditioning replacement air conditioning repair</p>
</div>

<!-- Footer -->
<div class="abs rule"></div>
<footer class="abs footer">
  <div class="fbrand"><span class="mark"></span>Brightwell Cooling Company</div>
  <div class="fsoc" style="left:131px"></div>
  <div class="fsoc" style="left:184px"></div>
  <div class="fsoc" style="left:236px"></div>
  <div class="fsoc" style="left:289px"></div>

  <div class="col" style="left:466px"><h3>Quick Links</h3><p>Home<br>About Us<br>Services<br>Hvac<br>Resources<br>Contact</p></div>
  <div class="col" style="left:653px"><h3>Our Services</h3><p>AC Repair<br>AC Installation<br>HVAC Maintenance<br>Duct Services</p></div>
  <div class="col" style="left:866px"><h3>Contact Info</h3><p style="line-height:32px">Tampa, Florida, United States<br>813-555-0192<br>hello@brightwellcooling.com</p></div>

  <div class="line"></div>
  <div class="copyr">©Copyright 2024 The Brightwell Cooling Company. All Rights Reserved.</div>
</footer>

</body>
</html>
```